Business card for consulting firm

We need a double-sided business card for consulting firm, VantoriX. The card should be professional but also creative and visually interesting.

Target Market(s)

Engineering and technology; transport industries; safety critical / heavy industry.

Contact Information for Business Card

See attached file with details.

Font styles to use
Sans Serif

```html
<!DOCTYPE html>
<html lang="en">
<head>
<meta charset="utf-8">
<title>VantoriX Business Card</title>
<link href="https://fonts.googleapis.com/css2?family=Montserrat:wght@400;600;700&display=swap" rel="stylesheet">
<style>
  :root {
    --page: #e9ecef;
    --card: #0b2233;
    --card-edge: #071826;
    --pattern-a: #12344b;
    --pattern-b: #0e2b3f;
    --accent: #2aa9e0;
    --ink: #ffffff;
    --ink-soft: #d9e4ec;
  }
  * { box-sizing: border-box; margin: 0; padding: 0; }
  html, body { width: 1200px; height: 1200px; overflow: hidden; }
  body {
    background: var(--page);
    font-family: "Montserrat", sans-serif;
    color: var(--ink);
    position: relative;
  }
  .card {
    position: absolute;
    left: 160px;
    width: 880px;
    height: 503px;
    background: var(--card);
    border-radius: 6px;
    overflow: hidden;
    box-shadow: 0 10px 30px rgba(7, 24, 38, 0.25);
  }
  .card--front { top: 60px; }
  .card--back { top: 637px; }

  .pattern-area {
    position: absolute;
    border-radius: 50%;
    background: radial-gradient(circle at 55% 45%, var(--pattern-a) 0%, var(--pattern-b) 60%, var(--card) 100%);
  }
  .card--front .pattern-area { left: -120px; top: 60px; width: 520px; height: 520px; }
  .card--back .pattern-area { left: -80px; top: -120px; width: 440px; height: 440px; }

  .brand { position: absolute; }
  .brand__name {
    display: block;
    font-weight: 700;
    color: var(--ink);
    letter-spacing: 0.04em;
    line-height: 1;
  }
  .brand__tagline {
    display: block;
    font-weight: 400;
    color: var(--ink);
    line-height: 1;
  }
  .card--front .brand { left: 230px; top: 190px; }
  .card--front .brand__name { font-size: 92px; }
  .card--front .brand__tagline { font-size: 30px; margin: 14px 0 0 150px; }

  .card--back .brand { left: 70px; top: 300px; }
  .card--back .brand__name { font-size: 58px; }
  .card--back .brand__tagline { font-size: 19px; margin: 10px 0 0 95px; }

  .divider {
    position: absolute;
    left: 470px;
    top: 150px;
    width: 2px;
    height: 230px;
    background: var(--ink-soft);
  }

  .contact { position: absolute; left: 505px; top: 150px; }
  .contact__name { font-size: 27px; font-weight: 700; letter-spacing: 0.03em; }
  .contact__credentials { font-size: 12.5px; font-weight: 600; color: var(--accent); margin-top: 6px; }
  .contact__role { font-size: 15px; font-weight: 700; letter-spacing: 0.05em; margin-top: 12px; }
  .contact__list { list-style: none; margin-top: 22px; }
  .contact__item {
    display: flex;
    align-items: flex-start;
    gap: 14px;
    font-size: 16px;
    line-height: 1.35;
    margin-bottom: 6px;
    color: var(--ink-soft);
  }
  .contact__icon { width: 18px; height: 18px; flex: none; margin-top: 2px; }
</style>
</head>
<body>
  <section class="card card--front" aria-label="Business card front">
    <div class="pattern-area" role="img" aria-label="Faint decorative pattern of overlapping dots in dark blue"></div>
    <div class="brand">
      <span class="brand__name">VANTORIX</span>
      <span class="brand__tagline">Safety &amp; Human Factors</span>
    </div>
  </section>

  <section class="card card--back" aria-label="Business card back">
    <div class="pattern-area" role="img" aria-label="Faint decorative pattern of overlapping dots in dark blue"></div>
    <div class="brand">
      <span class="brand__name">VANTORIX</span>
      <span class="brand__tagline">Safety &amp; Human Factors</span>
    </div>
    <div class="divider"></div>
    <div class="contact">
      <p class="contact__name">MAREN HOLLOWAY</p>
      <p class="contact__credentials">BA (Hons), M Psych Org, M Tech Mgt (HF)</p>
      <p class="contact__role">MANAGING DIRECTOR</p>
      <ul class="contact__list">
        <li class="contact__item">
          <svg class="contact__icon" viewBox="0 0 24 24" aria-hidden="true"><path fill="#2aa9e0" d="M6.6 10.8a15.1 15.1 0 0 0 6.6 6.6l2.2-2.2c.3-.3.7-.4 1-.2 1.1.4 2.3.6 3.6.6.6 0 1 .4 1 1V20c0 .6-.4 1-1 1C10.6 21 3 13.4 3 4c0-.6.4-1 1-1h3.5c.6 0 1 .4 1 1 0 1.3.2 2.5.6 3.6.1.3 0 .7-.2 1z"/></svg>
          <span>+61 (0)400 555 018</span>
        </li>
        <li class="contact__item">
          <svg class="contact__icon" viewBox="0 0 24 24" aria-hidden="true"><g fill="none" stroke="#2aa9e0" stroke-width="1.8"><circle cx="12" cy="12" r="9"/><ellipse cx="12" cy="12" rx="4" ry="9"/><path d="M3 12h18"/></g></svg>
          <span>www.vantorix.global<br>www.vantorix.com.au</span>
        </li>
        <li class="contact__item">
          <svg class="contact__icon" viewBox="0 0 24 24" aria-hidden="true"><path fill="#2aa9e0" d="M3 6h18v12H3z"/><path fill="none" stroke="#0b2233" stroke-width="1.6" d="M3 6l9 7 9-7"/></svg>
          <span>mholloway@vantorix.com.au</span>
        </li>
      </ul>
    </div>
  </section>
</body>
</html>
```